Business Card Design - TBW (company name)

Over 20 years of progressive technology design, migration and management experience that drives business objectives and streamlines operations. Continuously challenge conventions to meet and exceed business security, availability and functionality requirements. Maintain exceptional vendor relationships to ensure ongoing knowledge of emerging products and to secure preferred service agreements. Recruit and utilize top talent and foster a collegial environment that advances innovation and performance excellence. design logo using 3 arrows of different colors green, gold, blue

Industry/Entity Type

Progressive

Contact Information for Business Card

Martin K. Osgood
IT Strategist / Consultant

626.583.2904 MOsgood@tbwosgood.com 4817 Ferndale Court Pasadena, CA 91107

Colors
0255a3
f37122
fece3e

Requirements
Must have
• Note NEW EMAIL ADDRESS
• MOsgood@tbwosgood.com
• NOTE NEW ORDER of the work I do.
• Infrastructure – Systems – Cybersecurity
Nice to have
• main color should be orange

```html
<!DOCTYPE html>
<html lang="en">
<head>
<meta charset="utf-8">
<title>TBW Business Card – Martin K. Osgood</title>
<link rel="stylesheet" href="https://fonts.googleapis.com/css2?family=Michroma&family=Open+Sans:wght@400;600;700&display=swap">
<style>
  :root {
    --brand-blue: #0255a3;
    --brand-orange: #f37122;
    --brand-gold: #fece3e;
    --deep-blue: #0b3f6b;
    --mid-blue: #2f7fc0;
    --light-blue: #6fb3e6;
    --ink-grey: #4a4a4a;
    --paper: #ffffff;
    --canvas: #e9e9ec;
  }
  * { box-sizing: border-box; margin: 0; padding: 0; }
  html, body {
    width: 1200px; height: 784px; overflow: hidden;
    background: var(--canvas);
    font-family: "Open Sans", Arial, sans-serif;
  }
  .card {
    position: absolute;
    width: 540px; height: 309px;
    top: 237px;
    overflow: hidden;
    box-shadow: 0 2px 6px rgba(0,0,0,.12);
  }
  .card--back { left: 40px; background: var(--deep-blue); }
  .card--front { left: 620px; background: var(--paper); }

  .back-pattern {
    position: absolute; inset: 0;
    background: radial-gradient(ellipse at 75% 30%, var(--light-blue) 0%, var(--mid-blue) 45%, var(--deep-blue) 100%);
  }
  .back-brand {
    position: absolute; left: 0; right: 0; top: 70px;
    display: flex; align-items: center; justify-content: center; gap: 10px;
    color: var(--paper);
    font-family: "Michroma", Arial, sans-serif; font-size: 28px;
  }
  .brand-square { width: 22px; height: 22px; background: var(--brand-orange); }
  .back-name {
    position: absolute; left: 0; right: 0; top: 150px; text-align: center;
    color: var(--paper);
    font-family: "Michroma", Arial, sans-serif; font-size: 31px; letter-spacing: 1px;
  }
  .back-title {
    position: absolute; left: 0; right: 0; top: 198px; text-align: center;
    color: var(--paper);
    font-family: "Michroma", Arial, sans-serif; font-size: 12px; letter-spacing: 3px;
  }

  .front-brand {
    position: absolute; left: 28px; top: 80px;
    display: flex; align-items: center; gap: 8px;
    color: var(--brand-blue);
    font-family: "Michroma", Arial, sans-serif; font-size: 24px;
  }
  .front-name {
    position: absolute; left: 160px; top: 52px;
    color: var(--brand-blue);
    font-family: "Michroma", Arial, sans-serif; font-size: 26px; letter-spacing: 1px;
  }
  .front-title {
    position: absolute; left: 162px; top: 92px;
    color: var(--ink-grey);
    font-family: "Michroma", Arial, sans-serif; font-size: 10px; letter-spacing: 2.5px;
  }
  .title-rule {
    position: absolute; left: 160px; right: 0; top: 112px; height: 5px;
    background: var(--brand-blue);
  }
  .services-band {
    position: absolute; left: 0; right: 0; top: 160px; height: 22px;
    background: var(--brand-blue);
    color: var(--paper);
    font-family: "Michroma", Arial, sans-serif; font-size: 11px; letter-spacing: 3px;
    line-height: 22px; padding-left: 22px; white-space: nowrap;
  }
  .contact {
    position: absolute; left: 200px; right: 20px; top: 205px; text-align: center;
  }
  .contact-phone { color: var(--brand-blue); font-weight: 700; font-size: 22px; line-height: 28px; }
  .contact-email { color: var(--ink-grey); font-size: 14px; line-height: 20px; }
  .contact-address { color: var(--ink-grey); font-weight: 600; font-size: 15px; line-height: 22px; }
</style>
</head>
<body>
  <section class="card card--back" aria-label="Card back">
    <div class="back-pattern" role="img" aria-label="Blue background with a field of soft light-blue circles"></div>
    <div class="back-brand"><span class="brand-square"></span><span>TBW</span></div>
    <div class="back-name">MARTIN K. OSGOOD</div>
    <div class="back-title">IT STRATEGIST / CONSULTANT</div>
  </section>

  <section class="card card--front" aria-label="Card front">
    <div class="front-brand"><span class="brand-square"></span><span>TBW</span></div>
    <div class="front-name">MARTIN K. OSGOOD</div>
    <div class="front-title">IT STRATEGIST / CONSULTANT</div>
    <div class="title-rule"></div>
    <div class="services-band">INFRASTRUCTURE – SYSTEMS – CYBERSECURITY</div>
    <div class="contact">
      <p class="contact-phone">626.583.2904</p>
      <p class="contact-email">MOsgood@tbwosgood.com</p>
      <p class="contact-address">4817 Ferndale Court Pasadena, CA 91107</p>
    </div>
  </section>
</body>
</html>
```